Copper Ridge Resort & Marina - Boat Slips, Cabin Rentals, Floating Vacation Homes, & More

We need an 8'H x 16'W billboard for our Resort & marina, www.copperridgeresort.example. We'd like it to include: Lakefront Cabin Rentals, Floating Vacation Homes, and New Slips Summer 2022. We'd like it to be simple using the colors on our logo, similar to our business cards, and have our logo on it large. Maybe an arrow on the bottom pointing left that says 3 miles, possibly our website and phone number.

Target Market(s)

Lake People, Boaters

Industry/Entity Type

Resort & Marina (Recreation/Hospitality)

Font styles to use
Sans Serif
Other font styles liked:
• Simple/modern

Colors
0054AA
0677BA
7BADD7
CADEEF
E8F1F8
FFC000
F8CF3A
FAE287
FDF2CF
FEFAEE
F0912C
F2A743
F7CA91
FBE8D2
FDF5EE

Requirements
Must have
• Logo, Cabin Rentals, Floating Vacation Homes, New Slips Summer 2022
Nice to have
• An additional banner hanging from the bottom with an orange (or blue, colors from our logo) arrow pointing left, with white text saying: 3 miles 555-214-0867 www.copperridgeresort.example
Should not have
• Shouldn't be too busy

```html
<!DOCTYPE html>
<html lang="en">
<head>
<meta charset="utf-8">
<title>Copper Ridge Resort &amp; Marina — Billboard</title>
<link rel="stylesheet" href="https://fonts.googleapis.com/css2?family=Nunito+Sans:ital,wght@0,700;1,800;1,900&display=swap">
<style>
  :root {
    --page: #eef1f4;
    --brand-blue: #0a4c9e;
    --contact-band: #dfe2e6;
    --ink-navy: #1a3f92;
    --gold: #d9a300;
    --gold-light: #e6a21e;
    --orange: #e58a2c;
    --white: #ffffff;
    --photo-dark: #2a1a12;
    --photo-sky: #6a7a90;
    --photo-sun: #e8902c;
  }
  * { margin: 0; padding: 0; box-sizing: border-box; }
  html, body {
    width: 1200px; height: 800px; overflow: hidden;
    background: var(--page);
  }
  .billboard {
    position: absolute; left: 0; top: 184px;
    width: 1200px; height: 432px;
    font-family: "Nunito Sans", sans-serif;
  }
  .billboard svg { display: block; }
  .brand-name {
    font-weight: 700; font-style: normal;
    fill: var(--white);
  }
  .brand-name--main { font-size: 33px; letter-spacing: 1px; }
  .brand-name--sub { font-size: 15px; letter-spacing: 6px; }
  .offer { font-weight: 900; font-style: italic; font-size: 34px; fill: var(--white); }
  .offer-year { fill: var(--gold-light); }
  .bullet { fill: var(--orange); }
  .direction-arrow { fill: var(--gold); }
  .contact-phone { font-weight: 900; font-style: italic; font-size: 46px; fill: var(--ink-navy); }
  .contact-web { font-weight: 800; font-style: italic; font-size: 31px; fill: var(--ink-navy); }
  .contact-icon { fill: var(--orange); }
</style>
</head>
<body>
<div class="billboard">
  <svg width="1200" height="432" viewBox="0 0 1200 432" xmlns="http://www.w3.org/2000/svg">
    <defs>
      <linearGradient id="sunsetGrad" x1="0" y1="0" x2="0" y2="1">
        <stop offset="0" stop-color="#3a2418"/>
        <stop offset="0.2" stop-color="#5d6d84"/>
        <stop offset="0.45" stop-color="#c98a4a"/>
        <stop offset="0.56" stop-color="#f0a23a"/>
        <stop offset="0.7" stop-color="#9a6a3e"/>
        <stop offset="1" stop-color="#1e1510"/>
      </linearGradient>
    </defs>

    <rect class="photo" x="540" y="0" width="660" height="432" fill="url(#sunsetGrad)"
          role="img" aria-label="Sunset over the lake seen from a covered boat slip with wooden pillars and a moored boat"/>

    <polygon class="contact-band" points="0,326 675,326 718,432 0,432" fill="var(--contact-band)"/>
    <polygon class="brand-panel" points="0,0 547,0 675,326 0,326" fill="var(--brand-blue)"/>

    <text class="brand-name brand-name--main" x="247" y="104" text-anchor="middle">COPPER RIDGE</text>
    <text class="brand-name brand-name--sub" x="247" y="133" text-anchor="middle">resort &amp; marina</text>

    <circle class="bullet" cx="52" cy="180" r="4"/>
    <text class="offer" x="74" y="192">Lakefront Cabin Rentals</text>
    <circle class="bullet" cx="52" cy="218" r="4"/>
    <text class="offer" x="74" y="230">Floating Vacation Homes</text>
    <circle class="bullet" cx="52" cy="256" r="4"/>
    <text class="offer" x="74" y="268">New Slips Summer <tspan class="offer-year">2022</tspan></text>

    <polygon class="direction-arrow" points="34,301 75,282 75,295 645,295 640,308 75,308 75,321"/>

    <path class="contact-icon" d="M28,341 c3,-3 7,-3 9,0 l4,6 c1,2 0,4 -2,5 l-3,2 c2,5 6,9 11,11 l2,-3 c1,-2 3,-3 5,-2 l6,4 c3,2 3,6 0,8 l-3,3 c-10,4 -30,-16 -32,-28 z"/>
    <text class="contact-phone" x="76" y="381">555-214-0867</text>

    <g class="contact-icon">
      <circle cx="38" cy="405" r="13" fill="none" stroke="var(--orange)" stroke-width="3"/>
      <ellipse cx="38" cy="405" rx="5" ry="13" fill="none" stroke="var(--orange)" stroke-width="2.5"/>
      <line x1="25" y1="405" x2="51" y2="405" stroke="var(--orange)" stroke-width="2.5"/>
      <line x1="28" y1="398" x2="48" y2="398" stroke="var(--orange)" stroke-width="2"/>
      <line x1="28" y1="412" x2="48" y2="412" stroke="var(--orange)" stroke-width="2"/>
    </g>
    <text class="contact-web" x="76" y="418">www.copperridgeresort.example</text>
  </svg>
</div>
</body>
</html>
```